Trading journal (Corvanta Loop)

I need a design for trading journal application.
I would like to start from dark version of the design and the main goal that it should be pretty intuitive for everyone. I am going to create the app from scratch and I don't have any logo or branding colors, so it is up to you to choose a color scheme but it is a dark mode, so one of the colors would be black obviously.
The app will be available for web PC, Android and iOS.

There is google document with the requirements.
https://files.plomivex.net/sheet/7QwZrT2kLpN9vB4xHs0Jd8YcGm3FaUe6/view?mode=open

Target Market(s)

Professional traders

Industry/Entity Type

Trading

Colors

Designer to choose colors to be used in the design.

Requirements
Must have
• Dark mode design for PC and mobile views, the design must be pretty intuitive for everyone.
Nice to have
• Tooltips for something non obvious; popovers after completing some actions

```html
<!DOCTYPE html>
<html lang="en">
<head>
<meta charset="utf-8">
<title>Corvanta Loop — Dashboard</title>
<link href="https://fonts.googleapis.com/css2?family=Poppins:wght@400;500;600;700&display=swap" rel="stylesheet">
<style>
:root{
  --page:#e8ecef;
  --app:#111214;
  --side-top:#12242b;
  --side-bot:#151b1f;
  --panel:#1c1d21;
  --panel-head:#16171a;
  --line:#2a2c31;
  --text:#ffffff;
  --muted:#9a9ca3;
  --teal:#1fd1a0;
  --blue:#1e8ef0;
  --green:#22c55e;
  --red:#ef4444;
}
*{box-sizing:border-box;margin:0;padding:0}
html,body{width:1200px;height:810px;overflow:hidden;background:var(--page);font-family:'Poppins',sans-serif;color:var(--text)}
.stage{position:absolute;left:0;top:63px;width:1440px;height:820px;transform:scale(.8333);transform-origin:0 0}
.app{position:absolute;inset:0;background:var(--app);border-radius:30px;overflow:hidden}
.sidebar{position:absolute;left:0;top:0;width:84px;height:100%;background:linear-gradient(180deg,var(--side-top),var(--side-bot))}
.brand{position:absolute;left:8px;top:28px;width:68px;text-align:center;font-size:11px;font-weight:600;line-height:1.3;color:var(--teal)}
.nav-item{position:absolute;left:16px;width:52px;height:52px;border-radius:12px;display:flex;align-items:center;justify-content:center}
.nav-item.active{background:linear-gradient(135deg,#1aa6e6,#22c7d6)}
.nav-item svg{width:20px;height:20px;fill:none;stroke:#d8dde2;stroke-width:1.6}
.nav-item.active svg{stroke:#fff}
.main{position:absolute;left:124px;top:0;right:40px;height:100%}
.title{position:absolute;left:0;top:24px;font-size:24px;font-weight:600}
.account{position:absolute;left:955px;top:16px;width:184px;height:48px;border:1px solid var(--line);border-radius:8px;display:flex;align-items:center;padding:0 14px;gap:10px;font-size:12px;font-weight:500}
.account .chev{margin-left:auto;width:18px;height:18px;border-radius:50%;background:#23302b;display:flex;align-items:center;justify-content:center}
.bell{position:absolute;left:1172px;top:28px}
.badge{position:absolute;left:1187px;top:20px;width:16px;height:16px;border-radius:50%;background:var(--teal);color:#0c1a14;font-size:9px;font-weight:600;text-align:center;line-height:16px}
.avatar{position:absolute;left:1232px;top:20px;width:40px;height:40px;border-radius:50%;background:radial-gradient(circle at 40% 35%,#c9b59a,#4d6a8a 70%)}
.divider{position:absolute;left:0;right:0;top:80px;height:1px;background:var(--line)}
.greet{position:absolute;left:0;top:112px;font-size:18px;font-weight:500}
.updated{position:absolute;left:906px;top:118px;font-size:11px;color:#c8cad0;display:flex;align-items:center;gap:6px}
.import{position:absolute;left:1157px;top:105px;width:119px;height:40px;border-radius:20px;background:linear-gradient(90deg,#1a8ff0,#1fcfae);display:flex;align-items:center;justify-content:center;gap:8px;font-size:15px;font-weight:600}
.stat{position:absolute;top:169px;width:236px;height:122px;border-radius:14px;border:1px solid #2a2c31;padding:0 16px}
.stat .ico{position:absolute;left:16px;top:15px;width:40px;height:40px;border-radius:50%;background:rgba(255,255,255,.25);display:flex;align-items:center;justify-content:center}
.stat .ico svg{width:20px;height:20px;fill:none;stroke:#fff;stroke-width:1.6}
.stat .info{position:absolute;right:16px;top:17px;width:18px;height:18px;border:1.4px solid #b8bac0;border-radius:50%;font-size:11px;text-align:center;line-height:15px;color:#b8bac0}
.stat .value{position:absolute;left:16px;top:66px;font-size:20px;font-weight:700}
.stat .label{position:absolute;left:16px;top:95px;font-size:11px;color:#c4c6cc}
.s1{left:0;background:linear-gradient(135deg,#4c2d8a,#1f1c2a 55%,#1a1b1f)}
.s2{left:260px;background:linear-gradient(135deg,#1f4f99,#1b2433 55%,#1a1b1f)}
.s3{left:520px;background:linear-gradient(135deg,#1b7a4f,#1a2b25 55%,#1a1b1f)}
.s4{left:780px;background:linear-gradient(135deg,#a64a2c,#2a201d 55%,#1a1b1f)}
.s5{left:1040px;background:linear-gradient(135deg,#9b1f35,#2a1a1f 55%,#1a1b1f)}
.panel{position:absolute;top:339px;height:405px;border-radius:14px;background:var(--panel);overflow:hidden}
.pnl{left:0;width:659px}
.trades{left:699px;width:577px}
.panel-title{position:absolute;left:24px;top:30px;font-size:18px;font-weight:500;display:flex;align-items:center;gap:10px}
.i-small{width:18px;height:18px;border:1.4px solid #9a9ca3;border-radius:50%;font-size:11px;text-align:center;line-height:15px;color:#9a9ca3;font-weight:400}
.tabs{position:absolute;left:354px;top:24px;width:280px;height:36px;border:1px solid var(--line);border-radius:8px;background:#161719;display:flex;padding:3px}
.tab{flex:1;display:flex;align-items:center;justify-content:center;font-size:10px;font-weight:500;border-radius:6px;color:#d6d8dc}
.tab.active{background:#1d3a30;color:var(--teal);font-weight:600}
.chart{position:absolute;left:0;top:0}
.trades .panel-title{top:18px}
.trades .i-small{position:absolute;right:24px;top:20px}
.thead{position:absolute;left:0;right:0;top:58px;height:28px;background:var(--panel-head);font-size:11px;color:#c8cad0}
.thead span,.row span{position:absolute}
.row{position:absolute;left:0;right:0;height:53px;border-top:1px solid var(--line)}
.row:first-of-type{border-top:none}
.coin{left:24px;top:13px;width:28px;height:28px;border-radius:50%}
.sym{left:60px;top:17px;font-size:13px;font-weight:600}
.price{top:18px;font-size:12px;font-weight:500;display:flex;align-items:center;gap:6px}
.price::before{content:"";width:11px;height:11px;border-radius:50%;background:#6b6e75}
.entry{left:145px}.exit{left:266px}
.status{left:386px;top:17px;width:46px;height:18px;border-radius:9px;background:#101113;font-size:9px;font-weight:600;text-align:center;line-height:18px}
.status.open{color:var(--green)}.status.close{color:var(--red)}
.profit{right:24px;top:10px;text-align:right;font-size:12px;font-weight:600;line-height:1.2}
.profit small{display:block;font-size:9px;font-weight:400}
.up small{color:var(--green)}.down small{color:var(--red)}
</style>
</head>
<body>
<div class="stage">
 <div class="app">
  <aside class="sidebar">
   <div class="brand">Corvanta Loop</div>
   <div class="nav-item active" style="top:148px"><svg viewBox="0 0 20 20"><rect x="3" y="3" width="14" height="14" rx="3"/><path d="M8 3v14M8 10h9"/></svg></div>
   <div class="nav-item" style="top:204px"><svg viewBox="0 0 20 20"><rect x="3" y="3" width="14" height="14" rx="3"/><path d="M7 14v-3M10 14V9M13 14V6"/></svg></div>
   <div class="nav-item" style="top:260px"><svg viewBox="0 0 20 20"><rect x="3" y="4" width="14" height="13" rx="3"/><path d="M3 8h14M7 2v4M13 2v4M7 11h1M10 11h1M13 11h1M7 14h1M10 14h1"/></svg></div>
   <div class="nav-item" style="top:316px"><svg viewBox="0 0 20 20"><path d="M10 2l7 4v8l-7 4-7-4V6z"/><circle cx="10" cy="10" r="2.5"/></svg></div>
   <div class="nav-item" style="top:372px"><svg viewBox="0 0 20 20"><rect x="3" y="3" width="14" height="14" rx="3"/><circle cx="10" cy="8.5" r="2.5"/><path d="M6 15c1-2.5 7-2.5 8 0"/></svg></div>
   <div class="nav-item" style="top:744px"><svg viewBox="0 0 20 20"><path d="M11 4H6a2 2 0 0 0-2 2v8a2 2 0 0 0 2 2h5"/><path d="M9 10h8M14 7l3 3-3 3"/></svg></div>
  </aside>

  <main class="main">
   <h1 class="title">Dashboard</h1>
   <div class="account">
    <svg width="22" height="20" viewBox="0 0 22 20" fill="none" stroke="#1ea7f0" stroke-width="1.6"><rect x="2" y="4" width="17" height="13" rx="3"/><path d="M5 4l9-3 2 3"/><rect x="13" y="9" width="7" height="4" rx="1.5"/></svg>
    <span>IB #J208645...</span>
    <span class="chev"><svg width="8" height="6" viewBox="0 0 8 6"><path d="M1 1l3 3 3-3" stroke="#1fd1a0" stroke-width="1.5" fill="none"/></svg></span>
   </div>
   <svg class="bell" width="22" height="24" viewBox="0 0 22 24" fill="none" stroke="#cfd2d6" stroke-width="1.6"><path d="M5 17V10a6 6 0 0 1 12 0v7l2 2H3z"/><path d="M9 21a2 2 0 0 0 4 0"/></svg>
   <div class="badge">4</div>
   <div class="avatar" role="img" aria-label="User profile photo"></div>
   <div class="divider"></div>

   <div class="greet">Good day, Marin!</div>
   <div class="updated"><svg width="14" height="14" viewBox="0 0 14 14" fill="none" stroke="#c8cad0" stroke-width="1.4"><path d="M12 7a5 5 0 1 1-3-4.6"/><path d="M9 1v2.5h2.5"/></svg>LAST UPDATED: JAN 20, 2024 &nbsp;12:28 PM</div>
   <div class="import"><svg width="20" height="20" viewBox="0 0 20 20" fill="none" stroke="#fff" stroke-width="1.8"><path d="M17 10a7 7 0 1 1-4-6.3"/><path d="M10 10l6-6M12 4h4v4"/></svg>Import</div>

   <div class="stat s1"><div class="ico"><svg viewBox="0 0 20 20"><path d="M3 10l7-6 7 6v7H3z"/><path d="M6 14l3-3 2 2 3-3"/></svg></div><div class="info">i</div><div class="value">$1600</div><div class="label">TOTAL NET PROFIT</div></div>
   <div class="stat s2"><div class="ico"><svg viewBox="0 0 20 20"><rect x="3" y="4" width="14" height="12" rx="3"/><path d="M3 11h3l2-3 3 5 2-2h4"/></svg></div><div class="info">i</div><div class="value">50%</div><div class="label">AVERAGE WIN/LOSS</div></div>
   <div class="stat s3"><div class="ico"><svg viewBox="0 0 20 20"><path d="M3 17h14"/><rect x="4" y="9" width="2.5" height="6" rx="1"/><rect x="8.8" y="6" width="2.5" height="9" rx="1"/><rect x="13.5" y="3" width="2.5" height="12" rx="1"/></svg></div><div class="info">i</div><div class="value">304</div><div class="label">TOTAL # OF TRADES</div></div>
   <div class="stat s4"><div class="ico"><svg viewBox="0 0 20 20"><path d="M16 9a6 6 0 1 1-4-5.6"/><path d="M12 3h4v4M16 3l-5 5"/><path d="M11 8.5c-1-1-3-.7-3 .5s3 1 3 2.3-2 1.6-3 .6M9.5 6.5v1M9.5 12.5v1"/></svg></div><div class="info">i</div><div class="value">50%</div><div class="label">WIN RATE</div></div>
   <div class="stat s5"><div class="ico"><svg viewBox="0 0 20 20"><circle cx="9" cy="9" r="6"/><circle cx="14" cy="14" r="3.5"/><path d="M10.5 7c-.8-.8-3-.6-3 .5s3 .8 3 2-2 1.4-3 .6M9 5v1M9 11.5v1"/></svg></div><div class="info">i</div><div class="value">$1,097</div><div class="label">FEES &amp; COMMISSION</div></div>

   <section class="panel pnl">
    <div class="panel-title">Daily Net &nbsp;Cumulative P&amp;L <span class="i-small">i</span></div>
    <div class="tabs"><span class="tab">DAILY</span><span class="tab active">WEEKLY</span><span class="tab">MONTHLY</span></div>
    <svg class="chart" width="659" height="405" viewBox="0 0 659 405" font-family="Poppins, sans-serif">
     <defs>
      <linearGradient id="area" x1="0" y1="0" x2="0" y2="1">
       <stop offset="0" stop-color="#22e39a"/>
       <stop offset=".5" stop-color="#1a7f7a"/>
       <stop offset="1" stop-color="#1b2f45"/>
      </linearGradient>
     </defs>
     <g stroke="#3a3c42" stroke-dasharray="3 3" stroke-width="1">
      <line x1="98" y1="94" x2="634" y2="94"/><line x1="98" y1="126" x2="634" y2="126"/><line x1="98" y1="158" x2="634" y2="158"/><line x1="98" y1="190" x2="634" y2="190"/><line x1="98" y1="222" x2="634" y2="222"/><line x1="98" y1="254" x2="634" y2="254"/><line x1="98" y1="286" x2="634" y2="286"/><line x1="98" y1="318" x2="634" y2="318"/>
     </g>
     <g fill="#c8cad0" font-size="12" text-anchor="end">
      <text x="74" y="98">$6,000</text><text x="74" y="130">$5,000</text><text x="74" y="162">$4,000</text><text x="74" y="194">$3,000</text><text x="74" y="226">$2,000</text><text x="74" y="258">$1,000</text><text x="74" y="290">$0</text><text x="74" y="322">$-1,000</text>
     </g>
     <path d="M98 271 C120 266 130 258 142 254 C180 238 220 215 252 222 C300 232 320 296 363 296 C410 296 440 232 473 206 C510 178 545 165 584 160 C605 156 620 150 634 149 L634 318 L98 318 Z" fill="url(#area)" opacity=".9"/>
     <path d="M98 271 C120 266 130 258 142 254 C180 238 220 215 252 222 C300 232 320 296 363 296 C410 296 440 232 473 206 C510 178 545 165 584 160 C605 156 620 150 634 149" fill="none" stroke="#fff" stroke-width="1.6"/>
     <g fill="#111214" stroke="#fff" stroke-width="2.5">
      <circle cx="142" cy="254" r="7"/><circle cx="252" cy="222" r="7"/><circle cx="363" cy="296" r="7"/><circle cx="473" cy="206" r="7"/><circle cx="584" cy="160" r="7"/>
     </g>
     <g font-size="10" font-weight="600" fill="#fff" text-anchor="middle">
      <rect x="118" y="221" width="48" height="18" rx="9" fill="#101113"/><text x="142" y="234">$1,000</text>
      <rect x="228" y="189" width="48" height="18" rx="9" fill="#101113"/><text x="252" y="202">$2,000</text>
      <rect x="337" y="264" width="52" height="18" rx="9" fill="#101113"/><text x="363" y="277">-$300</text>
      <rect x="560" y="128" width="48" height="18" rx="9" fill="#101113"/><text x="584" y="141">$3,830</text>
     </g>
     <rect x="426" y="143" width="94" height="38" rx="19" fill="#101113"/>
     <circle cx="444" cy="162" r="9" fill="#22c55e"/>
     <path d="M444 167v-9M440 161l4-4 4 4" stroke="#0b1a10" stroke-width="1.8" fill="none"/>
     <text x="462" y="159" font-size="12" font-weight="600" fill="#fff">$2,500</text>
     <text x="462" y="171" font-size="8" fill="#c8cad0">JAN 14-20</text>
     <g fill="#c8cad0" font-size="11" text-anchor="middle">
      <text x="142" y="354">WEEK 1</text><text x="254" y="354">WEEK 2</text><text x="366" y="354">WEEK 3</text><text x="478" y="354">WEEK 4</text><text x="590" y="354">WEEK 5</text>
     </g>
    </svg>
   </section>

   <section class="panel trades">
    <div class="panel-title">Opened and Recent Trades</div>
    <span class="i-small">i</span>
    <div class="thead">
     <span style="left:16px;top:7px">SYMBOL</span><span style="left:141px;top:7px">ENTRY PRICE</span><span style="left:266px;top:7px">EXIT PRICE</span><span style="left:391px;top:7px">STATUS</span><span style="right:16px;top:7px">PROFIT</span>
    </div>
    <div style="position:absolute;left:0;right:0;top:87px">
     <div class="row" style="top:0"><span class="coin" style="background:#f7931a"></span><span class="sym">KRV</span><span class="price entry">1.271</span><span class="price exit">1.378</span><span class="status close">CLOSE</span><span class="profit up">+$320<small>+1.8%</small></span></div>
     <div class="row" style="top:53px"><span class="coin" style="background:#58bf00"></span><span class="sym">LUMA</span><span class="price entry">1.308</span><span class="price exit">1.22</span><span class="status open">OPEN</span><span class="profit up">+$90<small>+2.1%</small></span></div>
     <div class="row" style="top:106px"><span class="coin" style="background:#3a3d44"></span><span class="sym">ORB</span><span class="price entry">1.023</span><span class="price exit">1.378</span><span class="status open">OPEN</span><span class="profit up">+$136<small>+1.8%</small></span></div>
     <div class="row" style="top:159px"><span class="coin" style="background:#f3ba2f"></span><span class="sym">VXT</span><span class="price entry">1.209</span><span class="price exit">1.326</span><span class="status close">CLOSE</span><span class="profit down">-$206<small>-1.9%</small></span></div>
     <div class="row" style="top:212px"><span class="coin" style="background:#2775ca"></span><span class="sym">SDLR</span><span class="price entry">1.271</span><span class="price exit">1.378</span><span class="status open">OPEN</span><span class="profit up">+$320<small>+1.8%</small></span></div>
     <div class="row" style="top:265px"><span class="coin" style="background:#26a17b"></span><span class="sym">TCNX</span><span class="price entry">1.308</span><span class="price exit">1.22</span><span class="status close">CLOSE</span><span class="profit up">+$90<small>+2.1%</small></span></div>
    </div>
   </section>
  </main>
 </div>
</div>
</body>
</html>
```